I work in creative/artistic projects across different mediums.
It needs to communicate creativity, style, sexy, uniqueness, individuality and sophistication.
It should not look corporate.
Colours I like are black silver gold deep purple, chocolate, orchid.
It doesn't have to make use of all these colours.
I do not like bright primary colors.
Updates

Project Deadline Extended
Reason: Still in the communication process and to allow the person enough time to finish the design. Though i should know in the next day or two. Thank you.

Target Market(s)

creatives and companies wanting to inject creativity into thier business.

Industry/Entity Type

Work

Contact Information for Business Card

Lionel Crowthwick
0418359026
lionel@lionelcrowthwick.com

quietsilverhour.com.au

Requirements
Should not have
• Anything corporate OR OLD FASHIONED

```html
<!DOCTYPE html>
<html lang="en">
<head>
<meta charset="utf-8">
<title>Lionel Crowthwick — Business Card</title>
<link rel="stylesheet" href="https://fonts.googleapis.com/css2?family=Didact+Gothic&family=Arimo&display=swap">
<style>
  :root {
    --backdrop: #4d4a49;
    --card-black: #0a0b0b;
    --card-edge: #1d1716;
    --gold: #c9a566;
    --gold-light: #e6cc8c;
    --gold-text: #c4a264;
    --band-brown: #5a1f12;
    --band-dark: #2e0d08;
  }
  html, body {
    margin: 0;
    padding: 0;
    width: 1200px;
    height: 1000px;
    overflow: hidden;
    background: var(--backdrop);
  }
  .canvas {
    display: block;
    width: 1200px;
    height: 1000px;
  }
  .name {
    font-family: "Didact Gothic", "Tahoma", sans-serif;
    font-size: 56px;
    fill: var(--gold-text);
  }
  .contact {
    font-family: "Arimo", "Arial", sans-serif;
    font-size: 31px;
    fill: var(--gold-text);
  }
</style>
</head>
<body>
<svg class="canvas" viewBox="0 0 1200 1000" xmlns="http://www.w3.org/2000/svg">
  <defs>
    <linearGradient id="sheen" x1="0" y1="0" x2="1" y2="1">
      <stop offset="0" stop-color="#ffffff" stop-opacity="0.07"/>
      <stop offset="1" stop-color="#ffffff" stop-opacity="0"/>
    </linearGradient>
    <radialGradient id="band-tone" cx="0.5" cy="0.5" r="0.5">
      <stop offset="0.75" stop-color="var(--band-dark)"/>
      <stop offset="0.88" stop-color="var(--band-brown)"/>
      <stop offset="1" stop-color="var(--band-dark)"/>
    </radialGradient>
  </defs>

  <!-- card body -->
  <g class="card">
    <rect class="card-body" x="44" y="155" width="1110" height="683" fill="var(--card-black)"/>
    <rect class="card-edge" x="66" y="175" width="1068" height="643" fill="none" stroke="var(--card-edge)" stroke-width="10"/>
    <path class="card-sheen" d="M86 196 H1114 V215 C900 330 620 360 420 450 C260 520 150 640 86 760 Z" fill="url(#sheen)"/>
    <rect class="gold-frame" x="83" y="193" width="1034" height="609" fill="none" stroke="var(--gold)" stroke-width="7"/>
  </g>

  <!-- emblem ring -->
  <g class="emblem">
    <circle class="ring-band" cx="600" cy="468" r="192" fill="none" stroke="url(#band-tone)" stroke-width="50"
            role="img" aria-label="Ornamental band of gold floral scrolls on a deep brown patterned ground"/>
    <circle class="ring-outer" cx="600" cy="468" r="218" fill="none" stroke="var(--gold)" stroke-width="5"/>
    <circle class="ring-inner" cx="600" cy="468" r="166" fill="var(--card-black)" stroke="var(--gold)" stroke-width="6"/>
    <path class="ring-gloss" d="M420 360 A210 210 0 0 1 700 278" fill="none" stroke="var(--gold-light)" stroke-opacity="0.35" stroke-width="8" stroke-linecap="round"/>
  </g>

  <!-- name -->
  <text class="name" x="600" y="436" text-anchor="middle">Lionel</text>
  <text class="name" x="600" y="508" text-anchor="middle">Crowthwick</text>

  <!-- contact details -->
  <text class="contact phone" x="1070" y="690" text-anchor="end">0418359026</text>
  <text class="contact website" x="112" y="760">quietsilverhour.com.au</text>
  <text class="contact email" x="1085" y="760" text-anchor="end">lionel@lionelcrowthwick.com</text>
</svg>
</body>
</html>
```